Vell & Thorn Website Creation For Online Spirits Sales via MirrowDistillery.com

Want a Website developed that I will use to partner with Mirrow Distillery to sell my signature rum online. Mirrow Distillery will add the final code to make the website an e-commerce site. Website should have links to Social media pages, recipies, About, news and events, products. I have he domain name already just need a designer to make the website look professional. Need website capable of being viewed on iPhone and Android devices. Please use the color scheme that is on the label. The brand motto is: Celebrate Life With Family old and new friends. The bottle sent in the images will be replaced with and actual high resolution image of the bottle when it is produce on 27 DEC 21. Can give the selected designer access to develop the website. I have the hostiveno.com domain name. Final code will be added by a designer from MirrowDistillery.com to make it a e-commerce store.
Updates

I added more information to refine the design I wanted. I should have had this information available to the designers when I started the project.

Target Market(s)

Target Market is 25-50 year old who drink rum

Industry/Entity Type

Spirits. Using Website to sell Rum online

Number of Pages Required

1 page

Font styles to use
Sans Serif

Colors
00AB8E
00BBA5
67D7C9
C6EFE9
E9F9F6

Requirements
Must have
• Must look elegant and of high class. Rum is being market as a premium unnamed rum.
Nice to have
• Video of people drinking, smiling and celebrating

```html
<!DOCTYPE html>
<html lang="en">
<head>
<meta charset="utf-8">
<title>Vell &amp; Thorn</title>
<link rel="stylesheet" href="https://fonts.googleapis.com/css2?family=Oswald:wght@400;500&family=Lato:wght@400;700&display=swap">
<style>
:root{
  --green:#00AB8E;
  --green-2:#00BBA5;
  --mint:#C6EFE9;
  --mint-pale:#E9F9F6;
  --mint-mid:#B6EBE2;
  --ink:#222222;
  --text:#444444;
  --dark:#1B1B1B;
  --white:#FFFFFF;
  --amber:#C77A22;
  --amber-deep:#9A5514;
}
*{margin:0;padding:0;box-sizing:border-box}
html,body{width:1200px;height:2927px;overflow:hidden}
body{position:relative;background:var(--white);font-family:'Lato',sans-serif;color:var(--text)}
h1,h2,h3{font-weight:400}

/* header */
.site-header{position:absolute;left:0;top:0;width:1200px;height:139px;
  background:radial-gradient(ellipse 60% 120% at 30% 40%,#F2F2F2,transparent),radial-gradient(ellipse 50% 120% at 80% 60%,#EFEFEF,transparent),#E3E3E3}
.nav-link{position:absolute;top:57px;font-family:'Oswald',sans-serif;font-size:19px;color:var(--ink);text-transform:uppercase}
.nav-link.active{color:var(--green)}
.brand{position:absolute;left:450px;top:15px;width:300px;text-align:center}
.brand-dot{width:66px;height:66px;border-radius:50%;background:var(--ink);margin:0 auto 8px}
.brand-name{font-family:'Oswald',sans-serif;font-size:29px;color:var(--ink);letter-spacing:1.5px;line-height:1}
.user-icon{position:absolute;left:1096px;top:60px}

/* hero */
.hero{position:absolute;left:0;top:139px;width:1200px;height:698px;overflow:hidden}
.hero-photo{position:absolute;inset:0;background:
  radial-gradient(ellipse 18% 10% at 82% 22%,rgba(222,196,140,.95),transparent 70%),
  radial-gradient(ellipse 22% 14% at 80% 25%,rgba(200,170,110,.7),transparent 75%),
  radial-gradient(ellipse 7% 4% at 67% 62%,rgba(190,30,40,.85),transparent 70%),
  radial-gradient(ellipse 7% 4% at 77% 89%,rgba(190,30,40,.8),transparent 70%),
  radial-gradient(ellipse 30% 45% at 84% 72%,rgba(170,135,80,.75),transparent 75%),
  radial-gradient(ellipse 25% 35% at 75% 58%,rgba(40,30,25,.8),transparent 75%),
  radial-gradient(ellipse 55% 70% at 40% 45%,#4a4a4a,transparent 75%),
  linear-gradient(180deg,#262626 0%,#3a3a3a 40%,#2a2a2a 70%,#1f1f1f 100%)}
.hero-shade{position:absolute;inset:0;background:linear-gradient(90deg,rgba(0,0,0,.35) 0%,rgba(0,0,0,.1) 50%,transparent 65%)}
.hero-title{position:absolute;left:75px;top:210px;font-family:'Oswald',sans-serif;font-weight:500;font-size:54px;line-height:62px;color:var(--white);text-transform:uppercase;letter-spacing:.5px}
.hero-sub{position:absolute;left:75px;top:337px;width:640px;font-size:23px;line-height:34px;color:var(--white)}
.btn{position:absolute;display:flex;align-items:center;justify-content:center;background:var(--green);color:var(--white);font-family:'Oswald',sans-serif;font-size:20px;text-transform:uppercase;width:171px;height:57px}
.dots{position:absolute;display:flex;gap:13px}
.dot{width:12px;height:12px;border-radius:50%;background:var(--white)}
.dot.current{border:3px solid var(--white);background:var(--green)}

/* about */
.about{position:absolute;left:0;top:837px;width:1200px;height:599px;
  background:radial-gradient(ellipse 50% 60% at 70% 30%,#EDEDED,transparent),radial-gradient(ellipse 40% 50% at 20% 80%,#E4E4E4,transparent),#E0E0E0}
.bottles-photo{position:absolute;left:130px;top:50px;width:320px;height:510px;
  background:
  radial-gradient(ellipse 22% 38% at 40% 62%,rgba(214,138,48,1),transparent 80%),
  radial-gradient(ellipse 20% 34% at 66% 56%,rgba(200,122,36,.9),transparent 80%),
  radial-gradient(ellipse 18% 30% at 30% 48%,rgba(206,130,42,.9),transparent 80%),
  radial-gradient(ellipse 16% 12% at 40% 66%,rgba(198,239,233,.9),transparent 80%),
  radial-gradient(ellipse 30% 18% at 45% 15%,rgba(236,228,212,.8),transparent 80%),
  radial-gradient(ellipse 45% 48% at 48% 55%,rgba(160,90,25,.35),transparent 85%)}
.section-title{position:absolute;font-family:'Oswald',sans-serif;font-weight:400;font-size:50px;color:var(--ink);text-transform:uppercase;line-height:1}
.about-lead{position:absolute;left:524px;top:177px;width:580px;font-weight:700;font-size:24px;line-height:32px;color:var(--green)}
.about-body{position:absolute;left:524px;top:254px;width:565px;font-size:16.5px;line-height:28px;color:var(--text)}
.about-body p{margin-bottom:4px}

/* solutions */
.solutions{position:absolute;left:0;top:1436px;width:1200px;height:507px;background:var(--mint-pale);overflow:hidden}
.sol-funnel{position:absolute;left:0;top:0}
.solution-bottle{position:absolute;left:520px;top:105px;width:180px;height:402px;
  background:
  radial-gradient(ellipse 38% 42% at 50% 72%,rgba(208,132,42,1),transparent 85%),
  radial-gradient(ellipse 34% 12% at 50% 62%,rgba(198,239,233,.9),transparent 85%),
  radial-gradient(ellipse 16% 22% at 50% 12%,rgba(236,228,212,.95),transparent 85%)}
.sol-icon{position:absolute;width:82px;height:82px;border-radius:50%;background:var(--green);display:flex;align-items:center;justify-content:center}
.sol-item{position:absolute;font-size:16px;line-height:27px;color:var(--text)}
.sol-item h3{font-size:24px;font-weight:700;color:var(--green);line-height:1;margin-bottom:12px}
.sol-item.right-align{text-align:right}

/* testimonials */
.testimonial-photo{position:absolute;left:75px;top:2018px;width:511px;height:414px;background:
  radial-gradient(ellipse 30% 25% at 50% 15%,rgba(230,215,140,.9),transparent 80%),
  radial-gradient(ellipse 25% 30% at 20% 35%,rgba(90,100,60,.8),transparent 80%),
  radial-gradient(ellipse 25% 35% at 85% 55%,rgba(150,150,170,.6),transparent 80%),
  radial-gradient(ellipse 25% 30% at 50% 75%,rgba(220,210,190,.7),transparent 80%),
  linear-gradient(135deg,#5a5a34 0%,#9c8d4c 45%,#3e3c28 100%)}
.play{position:absolute;left:290px;top:2184px}
.quote{position:absolute;left:616px;top:2160px;width:520px;font-size:22px;line-height:36px;color:var(--ink)}
.quote-author{position:absolute;left:616px;top:2253px;font-size:19px;font-weight:700;color:var(--green)}
.dots.dark .dot{background:#555;width:13px;height:13px}
.dots.dark .dot.current{background:var(--green);border:none}

/* footer */
.site-footer{position:absolute;left:0;top:2506px;width:1200px;height:421px;background:var(--dark)}
.footer-top-rule{position:absolute;left:0;top:185px;width:1200px;height:1px;background:#3a3a3a}
.footer-brand{position:absolute;left:75px;top:40px;width:222px;text-align:center}
.footer-brand .brand-dot{background:var(--white);width:64px;height:64px}
.footer-brand .brand-name{color:var(--white);font-size:28px}
.footer-divider{position:absolute;left:342px;top:42px;width:1px;height:108px;background:#888}
.subscribe-label{position:absolute;left:376px;top:78px;font-family:'Oswald',sans-serif;font-weight:500;font-size:26px;color:var(--white);text-transform:uppercase}
.email-field{position:absolute;left:593px;top:66px;width:392px;height:61px;background:var(--white);font-family:'Oswald',sans-serif;font-size:18px;color:var(--ink);padding-left:18px;display:flex;align-items:center;text-transform:uppercase}
.subscribe-btn{position:absolute;left:985px;top:66px;width:141px;height:61px;background:var(--green);color:var(--white);font-family:'Oswald',sans-serif;font-size:22px;display:flex;align-items:center;justify-content:center;text-transform:uppercase}
.footer-nav{position:absolute;left:0;top:254px;width:1200px;display:flex;justify-content:center;gap:38px;font-family:'Oswald',sans-serif;font-size:19px;color:var(--white);text-transform:uppercase}
.copyright{position:absolute;left:0;top:300px;width:1200px;text-align:center;font-size:15px;color:#ddd}
.social{position:absolute;left:0;top:333px;width:1200px;display:flex;justify-content:center;gap:20px}
.social span{width:22px;height:22px;border-radius:50%;background:var(--white)}
</style>
</head>
<body>

<header class="site-header">
  <span class="nav-link active" style="left:75px">Home</span>
  <span class="nav-link" style="left:155px">About</span>
  <span class="nav-link" style="left:241px">Products</span>
  <span class="nav-link" style="left:357px">Recipes</span>
  <div class="brand">
    <div class="brand-dot"></div>
    <div class="brand-name">VELL &amp; THORN</div>
  </div>
  <span class="nav-link" style="left:809px">News &amp; Events</span>
  <span class="nav-link" style="left:962px">Contact</span>
  <svg class="user-icon" width="22" height="20" viewBox="0 0 22 20" aria-label="Account"><circle cx="11" cy="6" r="5" fill="#00AB8E"/><path d="M1 20c0-6 4-8 10-8s10 2 10 8z" fill="#00AB8E"/></svg>
</header>

<section class="hero">
  <div class="hero-photo" role="img" aria-label="Dark wooden table with a wooden gift box holding red-capped wine bottles in straw"></div>
  <div class="hero-shade"></div>
  <h1 class="hero-title">Set up your e-commerce<br>with Vell &amp; Thorn</h1>
  <p class="hero-sub">The&nbsp; No. 1 solution for direct to consumer&nbsp; E-Commerce services&nbsp; within the beverage industry.</p>
  <span class="btn" style="left:75px;top:426px">Read More</span>
  <div class="dots" style="left:75px;top:632px">
    <span class="dot current"></span><span class="dot"></span><span class="dot"></span><span class="dot"></span>
  </div>
</section>

<section class="about">
  <div class="bottles-photo" role="img" aria-label="Three bottles of Vell &amp; Thorn rum with teal labels"></div>
  <h2 class="section-title" style="left:524px;top:108px">About Vell &amp; Thorn</h2>
  <p class="about-lead">The pioneer of the white-label approach within the Direct To Consumer channel.</p>
  <div class="about-body">
    <p>Vell &amp; Thorn offers custom e-commerce solutions for emerging and established brands looking to use technology as a tool for reaching new customers.</p>
    <p>Vell &amp; Thorn fulfillment services operate through a national network of licensed retailers, shipping carriers, and customer service professionals to guarantee the best fulfillment and logistics practices.</p>
  </div>
  <span class="btn" style="left:524px;top:453px">Read More</span>
</section>

<section class="solutions">
  <svg class="sol-funnel" width="1200" height="507" viewBox="0 0 1200 507"><polygon points="377,0 823,0 710,507 494,507" fill="#B6EBE2"/></svg>
  <h2 class="section-title" style="left:0;width:1200px;text-align:center;top:42px">Our Solutions</h2>
  <div class="solution-bottle" role="img" aria-label="Bottle of Vell &amp; Thorn rum"></div>

  <div class="sol-item right-align" style="left:92px;top:102px;width:250px">
    <h3>White-Label</h3>
    Back in 2014, Mirrow Distillery brought technology and customization into the beverage industry by being the first company to offer
  </div>
  <div class="sol-icon" style="left:367px;top:108px">
    <svg width="44" height="44" viewBox="0 0 44 44"><path d="M4 6v14l20 20 16-16L20 4H6z" fill="#fff"/><circle cx="12" cy="12" r="3.5" fill="#00AB8E"/></svg>
  </div>

  <div class="sol-item right-align" style="left:86px;top:316px;width:320px">
    <h3>Subscriptions</h3>
    Subscriptions models are among some of the most successful strategies within the e-commerce arena.
  </div>
  <div class="sol-icon" style="left:430px;top:317px">
    <svg width="40" height="40" viewBox="0 0 40 40"><rect x="4" y="7" width="32" height="29" rx="2" fill="#fff"/><g fill="#00AB8E"><rect x="9" y="17" width="5" height="4"/><rect x="17.5" y="17" width="5" height="4"/><rect x="26" y="17" width="5" height="4"/><rect x="9" y="24" width="5" height="4"/><rect x="17.5" y="24" width="5" height="4"/><rect x="26" y="24" width="5" height="4"/></g><rect x="11" y="3" width="3" height="7" fill="#fff"/><rect x="26" y="3" width="3" height="7" fill="#fff"/></svg>
  </div>

  <div class="sol-icon" style="left:754px;top:108px">
    <svg width="42" height="36" viewBox="0 0 42 36"><path d="M3 3v30h36" stroke="#fff" stroke-width="3" fill="none"/><g fill="#fff"><rect x="9" y="18" width="5" height="12"/><rect x="17" y="10" width="5" height="20"/><rect x="25" y="15" width="5" height="15"/><rect x="33" y="8" width="5" height="22"/></g></svg>
  </div>
  <div class="sol-item" style="left:856px;top:102px;width:270px">
    <h3>Analytics Suite</h3>
    Mirrow Distillery' proprietary CRM and interactive reporting platform provides analytics on traffic sourcing, conversion ratios, demographics.
  </div>

  <div class="sol-icon" style="left:691px;top:317px">
    <svg width="44" height="36" viewBox="0 0 44 36"><rect x="7" y="3" width="30" height="22" rx="2" fill="none" stroke="#fff" stroke-width="3.5"/><rect x="2" y="28" width="40" height="5" rx="2" fill="#fff"/></svg>
  </div>
  <div class="sol-item" style="left:793px;top:316px;width:320px">
    <h3>Direct Marketing</h3>
    Mirrow Distillery' Direct Marketing services are a tool for brands to directly engage with tens of thousands of wine &amp; spirits buyers.
  </div>
</section>

<section>
  <div class="testimonial-photo" role="img" aria-label="Video still of friends laughing and toasting with wine outdoors"></div>
  <svg class="play" width="84" height="84" viewBox="0 0 84 84" aria-label="Play video"><circle cx="42" cy="42" r="38" fill="none" stroke="#fff" stroke-width="6"/><polygon points="33,24 62,42 33,60" fill="#fff"/></svg>
  <h2 class="section-title" style="left:616px;top:2078px">Testimonials</h2>
  <p class="quote">“We would probably not be where we are today had it not been for Vell &amp; Thorn partnership”.</p>
  <p class="quote-author">Delia R.</p>
  <div class="dots dark" style="left:616px;top:2353px">
    <span class="dot current"></span><span class="dot"></span><span class="dot"></span><span class="dot"></span>
  </div>
</section>

<footer class="site-footer">
  <div class="footer-brand">
    <div class="brand-dot"></div>
    <div class="brand-name">VELL &amp; THORN</div>
  </div>
  <div class="footer-divider"></div>
  <span class="subscribe-label">Subscribe Email</span>
  <div class="email-field">Email Address</div>
  <span class="subscribe-btn">Subscribe</span>
  <div class="footer-top-rule"></div>
  <nav class="footer-nav">
    <span>Home</span><span>About</span><span>Products</span><span>Recipes</span><span>News &amp; Events</span><span>Contact</span>
  </nav>
  <p class="copyright">© Copyright 2021. CompanyName All rights reserved</p>
  <div class="social" aria-label="Social media links">
    <span></span><span></span><span></span><span></span><span></span>
  </div>
</footer>

</body>
</html>
```